Lantern Business Cards

Need business cards for my employees at my restaurant.

Needs to include:
Our Logo
Lantern Bowls & Brews
Name: Nora Pettigrew
Title : Owner
Address: 487 Mirella Ave. Kestrel Harbor, KH 86519
Web: www.lanternkestrel.com
Phone: 555-555-0147
Cell: 555-555-0192
Email: info@lanternkestrel.com

```html
<!DOCTYPE html>
<html lang="en">
<head>
<meta charset="utf-8">
<title>Lantern Bowls &amp; Brews — Business Card</title>
<link rel="stylesheet" href="https://fonts.googleapis.com/css2?family=Montserrat:wght@400;500;700;800&display=swap">
<style>
  :root{
    --backdrop:#2a2a2c;
    --card:#1f1f20;
    --card-deep:#151516;
    --red:#c8202f;
    --white:#f2f2f2;
    --grey:#bdbdbd;
    --rule:#5a5a5a;
    --ghost:#2e2e30;
  }
  *{margin:0;padding:0;box-sizing:border-box}
  html,body{width:1200px;height:947px;overflow:hidden;background:var(--backdrop);font-family:"Montserrat",sans-serif}
  .canvas{position:relative;width:1200px;height:947px}
  .card{position:absolute;left:250px;width:700px;height:400px;border-radius:18px;overflow:hidden;background:var(--card)}
  .card--front{top:53px;background:var(--card-deep)}
  .card--back{top:494px}

  .front-pattern{position:absolute;inset:0;background:radial-gradient(ellipse at 75% 35%,#3a3a3c 0%,#242426 45%,#151516 100%)}
  .front-brand{position:absolute;left:0;right:0;top:135px;text-align:center}
  .brand-name{display:inline-flex;align-items:center;gap:18px;color:var(--red);font-weight:800;font-size:76px;letter-spacing:4px;line-height:1}
  .brand-dot{width:22px;height:22px;border-radius:50%;background:var(--white)}
  .tagline{display:flex;align-items:center;justify-content:center;gap:14px;margin-top:14px;color:var(--white);font-weight:500;font-size:15px;letter-spacing:3px}
  .tagline::before,.tagline::after{content:"";width:110px;height:1px;background:var(--white)}

  .back-mark{position:absolute;right:30px;top:-20px;width:300px;height:230px;background:radial-gradient(ellipse,#262628 0%,rgba(31,31,32,0) 70%)}
  .ghost-name{position:absolute;left:-6px;bottom:8px;font-weight:800;font-size:128px;letter-spacing:6px;color:var(--ghost);line-height:1}
  .ghost-tag{position:absolute;left:14px;bottom:140px;font-weight:500;font-size:14px;letter-spacing:4px;color:var(--ghost)}

  .details{position:absolute;left:300px;top:64px;width:370px;color:var(--white)}
  .person-name{color:var(--red);font-weight:700;font-size:30px;letter-spacing:1px;line-height:1}
  .person-title{font-size:15px;margin-top:6px;color:var(--white)}
  .address{font-size:13px;margin-top:34px;color:var(--white)}
  .rule{height:1px;background:var(--rule);margin:12px 0 14px}
  .contacts{display:grid;grid-template-columns:auto 1fr;column-gap:26px;row-gap:10px;font-size:13px}
  .contact{display:flex;align-items:center;gap:8px}
  .contact svg{width:14px;height:14px;flex:none}
</style>
</head>
<body>
<div class="canvas">

  <section class="card card--front">
    <div class="front-pattern" role="img" aria-label="Repeating tone-on-tone brand pattern across the card face"></div>
    <div class="front-brand">
      <div class="brand-name"><span class="brand-dot"></span>LANTERN</div>
      <div class="tagline">BOWLS AND BREWS</div>
    </div>
  </section>

  <section class="card card--back">
    <div class="back-mark" role="img" aria-label="Faint oversized brand emblem in the corner"></div>
    <div class="ghost-tag">BOWLS AND BREWS</div>
    <div class="ghost-name">LANTERN</div>

    <div class="details">
      <h1 class="person-name">NORA PETTIGREW</h1>
      <p class="person-title">Owner</p>
      <p class="address">487 Mirella Ave. Kestrel Harbor, KH 86519</p>
      <div class="rule"></div>
      <div class="contacts">
        <span class="contact">
          <svg viewBox="0 0 14 14"><rect x="3.5" y="1" width="7" height="12" rx="1.5" fill="none" stroke="#c8202f" stroke-width="1.4"/></svg>
          555-555-0192
        </span>
        <span class="contact">
          <svg viewBox="0 0 14 14"><rect x="1" y="3" width="12" height="8" fill="#c8202f"/><path d="M1 3l6 4.5L13 3" fill="none" stroke="#1f1f20" stroke-width="1"/></svg>
          info@lanternkestrel.com
        </span>
        <span class="contact">
          <svg viewBox="0 0 14 14"><path d="M3 1.5l2.2 2.6-1.2 1.6c.9 1.8 2.4 3.3 4.2 4.2l1.6-1.2 2.6 2.2-1.4 1.7C6.2 12.6 1.4 7.8 1.3 2.9z" fill="#c8202f"/></svg>
          555-555-0147
        </span>
        <span class="contact">
          <svg viewBox="0 0 14 14"><circle cx="7" cy="7" r="5.8" fill="none" stroke="#c8202f" stroke-width="1.3"/><ellipse cx="7" cy="7" rx="2.4" ry="5.8" fill="none" stroke="#c8202f" stroke-width="1"/><path d="M1.2 7h11.6" stroke="#c8202f" stroke-width="1"/></svg>
          www.lanternkestrel.com
        </span>
      </div>
    </div>
  </section>

</div>
</body>
</html>
```